E-book cover required. Title is Oda, author Clara J Penrod. Would like large title at top and smaller name at bottom. Book is apocolyptic novel and design needs to reference blood. Simple would be best.

```html
<!DOCTYPE html>
<html lang="en">
<head>
<meta charset="utf-8">
<title>Oda — Clara J Penrod</title>
<link rel="stylesheet" href="https://fonts.googleapis.com/css2?family=Rubik+Distressed&family=Questrial&display=swap">
<style>
  :root {
    --page: #ffffff;
    --night: #000000;
    --title-ink: #ffffff;
    --author-ink: #f4f1ec;
    --water-deep: #0a0603;
    --water-mid: #2b1606;
    --water-glow: #6b3410;
    --blood: #7a0c08;
  }
  html, body {
    margin: 0;
    padding: 0;
    width: 1200px;
    height: 900px;
    overflow: hidden;
    background: var(--page);
  }
  .canvas {
    position: relative;
    width: 1200px;
    height: 900px;
    background: var(--page);
  }
  .book-cover {
    position: absolute;
    left: 294px;
    top: 0;
    width: 616px;
    height: 900px;
    background: var(--night);
    overflow: hidden;
  }
  .cover-scene {
    position: absolute;
    left: 0;
    top: 340px;
    width: 616px;
    height: 560px;
    background:
      radial-gradient(ellipse 60px 40px at 530px 405px, rgba(122, 12, 8, 0.55), transparent 70%),
      radial-gradient(ellipse 120px 160px at 285px 390px, rgba(150, 80, 30, 0.35), transparent 70%),
      linear-gradient(180deg, var(--night) 0%, var(--night) 52%, var(--water-deep) 62%, var(--water-mid) 78%, var(--water-glow) 100%);
  }
  .title {
    position: absolute;
    left: 0;
    top: 0;
    width: 616px;
    height: 345px;
  }
  .title text {
    font-family: "Rubik Distressed", "Impact", sans-serif;
    fill: var(--title-ink);
  }
  .author {
    position: absolute;
    right: 34px;
    bottom: 36px;
    margin: 0;
    font-family: "Questrial", "Helvetica Neue", sans-serif;
    font-weight: 400;
    font-size: 38px;
    letter-spacing: 0.5px;
    line-height: 1;
    color: var(--author-ink);
    text-transform: uppercase;
    white-space: nowrap;
  }
</style>
</head>
<body>
  <main class="canvas">
    <article class="book-cover">
      <div class="cover-scene" role="img" aria-label="Night photograph of a woman in a pale dress wading waist-deep into dark, amber-lit water, seen from behind"></div>
      <svg class="title" viewBox="0 0 616 345" aria-label="Oda" role="img">
        <text x="0" y="338" font-size="540" textLength="616" lengthAdjust="spacingAndGlyphs">ODA</text>
      </svg>
      <p class="author">Clara J Penrod</p>
    </article>
  </main>
</body>
</html>
```